"Hollow Lanterns" Women's Fiction Book Cover

The title of the book is "Hollow Lanterns," and the author name is M.L. Dorn. It's women's fiction, but with a subtle supernatural flair. I'm just looking for something that fits the back cover copy (below). Surprise me!

When fleeing your past leads you straight to your future...
Lucinda Marwell's seemingly perfect life in Ashmont Heights comes crashing down around her when her fiancé announces that he’s in love with her cousin. Heartbroken and reckless, she crashes her car on a winding coastal road—an accident that should have killed, or at least paralyzed her. Instead, she awakens mysteriously unharmed, rescued by what she initially believes to be an angel. Later, she finds out her hero is an enigmatic Irish paramedic named Tobias.
Stranded in the idyllic town of Fernwick Cove, Lucinda finds herself working at a charming inn and, for the first time, feeling like she belongs somewhere. The close-knit community embraces her, and she’s drawn to Tobias despite his obvious secrets. But Tobias is running from a dangerous past—his supernatural gift of healing nearly cost him everything when he couldn’t save a Chicago mob boss’s son.
As Lucinda and Tobias grow closer, Tobias struggles to keep his abilities hidden. But when stories of miraculous healings in Fernwick Cove begin surfacing on social media, his past catches up with him. When a Chicago reporter sent by a vengeful mob boss closes in, Tobias must choose between protecting his secret and finally facing up to his fears.
In a town where everyone knows everyone else's business, some secrets are too powerful to stay buried.
A heartwarming tale of second chances, supernatural gifts, and finding home in the most unexpected places.

Target Market(s)

women ages 20-70

Requirements
Must have
• illustrated, brightly colored, whimsical
Nice to have
• see description

```html
<!DOCTYPE html>
<html lang="en">
<head>
<meta charset="utf-8">
<title>Hollow Lanterns — Cover Wrap</title>
<link href="https://fonts.googleapis.com/css2?family=Cinzel:wght@400;600;700&family=Poppins:ital,wght@0,400;0,600;0,700;1,400&display=swap" rel="stylesheet">
<style>
  :root {
    --page-bg: #f4f6f6;
    --teal: #5aa6a3;
    --teal-light: #7cc0bc;
    --teal-dark: #2d6e6b;
    --ink-teal: #2a6461;
    --headline-red: #7b3a2c;
    --title-top: #e9fbfa;
    --title-bottom: #5fc4c4;
    --white: #ffffff;
    --art-deep: #17383e;
    --art-mid: #2f6f78;
    --art-glow: #8fd8df;
  }
  * { margin: 0; padding: 0; box-sizing: border-box; }
  html, body { width: 1200px; height: 1200px; overflow: hidden; background: var(--page-bg); }
  .canvas { position: relative; width: 1200px; height: 1200px; display: flex; align-items: center; justify-content: center; }
  .cover-wrap { display: flex; height: 720px; box-shadow: 0 18px 40px rgba(0,0,0,.12); }

  .back-cover, .front-cover, .spine {
    height: 100%;
    background: radial-gradient(ellipse at 40% 30%, var(--teal-light) 0%, var(--teal) 55%, #4c9895 100%);
  }

  /* Back cover */
  .back-cover { width: 470px; padding: 44px 22px 30px 26px; font-family: "Poppins", sans-serif; color: var(--ink-teal); }
  .back-headline { font-family: "Cinzel", serif; font-weight: 600; font-size: 17px; line-height: 1.25; color: var(--headline-red); text-align: center; margin-bottom: 14px; letter-spacing: .3px; }
  .back-art {
    float: right; width: 186px; height: 318px; margin: 120px 4px 8px 12px;
    background: radial-gradient(ellipse at 50% 40%, var(--art-mid) 0%, var(--art-deep) 70%);
    border-radius: 6px;
    box-shadow: 0 0 14px 6px rgba(143,216,223,.35);
  }
  .blurb p { font-size: 12px; line-height: 1.42; margin-bottom: 11px; }
  .blurb .closing em { font-style: italic; }

  /* Spine */
  .spine { width: 56px; border-left: 1px solid rgba(0,0,0,.08); border-right: 1px solid rgba(0,0,0,.08); display: flex; flex-direction: column; align-items: center; justify-content: space-between; padding: 26px 0 28px; }
  .spine-title { writing-mode: vertical-rl; font-family: "Cinzel", serif; font-size: 26px; letter-spacing: 4px; color: var(--title-top); }
  .spine-author { writing-mode: vertical-rl; font-family: "Poppins", sans-serif; font-weight: 600; font-size: 18px; letter-spacing: 5px; color: var(--white); }

  /* Front cover */
  .front-cover { width: 470px; display: flex; flex-direction: column; align-items: center; padding: 30px 26px 24px; }
  .book-title { font-family: "Cinzel", serif; font-weight: 400; text-align: center; font-size: 66px; line-height: .98; letter-spacing: 2px;
    background: linear-gradient(180deg, var(--title-top) 0%, var(--title-bottom) 100%);
    -webkit-background-clip: text; background-clip: text; color: transparent;
    filter: drop-shadow(0 2px 2px rgba(20,60,60,.45)); }
  .cover-art {
    position: relative; width: 420px; height: 500px; margin-top: 16px;
    background: radial-gradient(ellipse at 65% 25%, var(--art-glow) 0%, var(--art-mid) 35%, var(--art-deep) 85%);
    border-radius: 6px;
    box-shadow: 0 0 16px 6px rgba(143,216,223,.35);
  }
  .tagline { position: absolute; top: 14px; left: 0; right: 0; padding: 0 34px; text-align: center; font-family: "Poppins", sans-serif; font-weight: 600; font-size: 13px; line-height: 1.3; color: var(--white); }
  .author-name { margin-top: 22px; font-family: "Poppins", sans-serif; font-weight: 700; font-size: 36px; letter-spacing: 14px; color: var(--white); }
</style>
</head>
<body>
<main class="canvas">
  <div class="cover-wrap">
    <section class="back-cover">
      <h2 class="back-headline">When fleeing your past leads you<br>straight to your future...</h2>
      <div class="back-art" role="img" aria-label="Illustration of the paramedic hero standing in misty blue light"></div>
      <div class="blurb">
        <p>Lucinda Marwell’s seemingly perfect life in Ashmont Heights comes crashing down around her when her fiancé announces that he’s in love with her cousin. Heartbroken and reckless, she crashes her car on a winding coastal road—an accident that should have killed, or at least paralyzed her. Instead, she awakens mysteriously unharmed, rescued by what she initially believes to be an angel. Later, she finds out her hero is an enigmatic Irish paramedic named Tobias.</p>
        <p>Stranded in the idyllic town of Fernwick Cove, Lucinda finds herself working at a charming inn and, for the first time, feeling like she belongs somewhere. The close-knit community embraces her, and she’s drawn to Tobias despite his obvious secrets. But Tobias is running from a dangerous past—his supernatural gift of healing nearly cost him everything when he couldn’t save a Chicago mob boss’s son.</p>
        <p>As Lucinda and Tobias grow closer, Tobias struggles to keep his abilities hidden. But when stories of miraculous healings in Fernwick Cove begin surfacing on social media, his past catches up with him. When a Chicago reporter sent by a vengeful mob boss closes in, Tobias must choose between protecting his secret and finally facing up to his fears.</p>
        <p class="closing">In a town where everyone knows everyone else’s business, <em>some secrets are too powerful to stay buried.</em></p>
      </div>
    </section>

    <section class="spine">
      <span class="spine-title">HOLLOW LANTERNS</span>
      <span class="spine-author">DORN</span>
    </section>

    <section class="front-cover">
      <h1 class="book-title">HOLLOW<br>LANTERNS</h1>
      <div class="cover-art" role="img" aria-label="Illustration of a glowing paramedic watching over a woman resting in a hospital bed, wisps of light swirling around them">
        <p class="tagline">A heartwarming tale of second chances, supernatural gifts, and finding home in the most unexpected places.</p>
      </div>
      <p class="author-name">M.L. DORN</p>
    </section>
  </div>
</main>
</body>
</html>
```